Book Cover "Venice"

Creation of a cover (14 x 20.5 cm + bleed area) for a book:
Image: “BrumeVerte” (Tiff joined)
AUTHOR: Corinne Valmer
TITLE: The murmurs of Lorient
PUBLISHER: Editions Pluvane (AT THE BOTTOM OF THE COVER)

Target Market(s)

Readers of romantic novels

Industry/Entity Type

Book

```html
<!DOCTYPE html>
<html lang="en">
<head>
<meta charset="utf-8">
<title>The murmurs of Lorient — Corinne Valmer</title>
<link rel="stylesheet" href="https://fonts.googleapis.com/css2?family=Cinzel:wght@400;500&family=Jost:ital,wght@0,400;1,400&display=swap">
<style>
  :root {
    --backdrop: #d9b98c;
    --sky-top: #4e1424;
    --sky-upper: #8e1a24;
    --sky-mid: #c8221f;
    --sky-glow: #e6391f;
    --sky-low: #b52018;
    --ground: #1a0808;
    --title-ink: #ead5ae;
    --publisher-ink: #ee5a2a;
  }
  html, body {
    margin: 0;
    padding: 0;
    width: 1200px;
    height: 1200px;
    overflow: hidden;
    background: var(--backdrop);
  }
  .cover {
    position: absolute;
    left: 236px;
    top: 73px;
    width: 729px;
    height: 1053px;
    overflow: hidden;
  }
  .cover-photo {
    position: absolute;
    inset: 0;
    background:
      radial-gradient(ellipse 70% 30% at 55% 62%, rgba(240, 70, 35, 0.55), transparent 70%),
      linear-gradient(180deg,
        var(--sky-top) 0%,
        var(--sky-upper) 12%,
        var(--sky-mid) 30%,
        var(--sky-low) 45%,
        var(--sky-glow) 62%,
        var(--sky-low) 74%,
        #3a0d0e 86%,
        var(--ground) 100%);
  }
  .author {
    position: absolute;
    left: 0;
    right: 0;
    top: 64px;
    margin: 0;
    text-align: center;
    font-family: "Jost", sans-serif;
    font-weight: 400;
    font-size: 40px;
    line-height: 1;
    letter-spacing: 0.08em;
    color: var(--title-ink);
    text-transform: uppercase;
  }
  .title {
    margin: 0;
    font-weight: 500;
  }
  .title-line {
    position: absolute;
    left: 0;
    right: 0;
    text-align: center;
    font-family: "Cinzel", serif;
    line-height: 1;
    color: var(--title-ink);
    text-transform: uppercase;
  }
  .title-small { font-size: 58px; }
  .title-large { font-size: 90px; }
  .title-largest { font-size: 108px; }
  .line-the { top: 296px; }
  .line-murmurs { top: 355px; }
  .line-of { top: 445px; }
  .line-lorient { top: 504px; }
  .publisher {
    position: absolute;
    left: 0;
    right: 0;
    top: 964px;
    margin: 0;
    text-align: center;
    font-family: "Jost", sans-serif;
    font-style: italic;
    font-weight: 400;
    font-size: 29px;
    line-height: 1;
    letter-spacing: 0.04em;
    color: var(--publisher-ink);
    text-transform: uppercase;
  }
</style>
</head>
<body>
  <main class="cover">
    <div class="cover-photo" role="img" aria-label="BrumeVerte photograph: a blazing red sunset sky over the silhouetted domes and bell towers of a waterfront basilica, with glowing street lanterns in the foreground"></div>
    <p class="author">Corinne Valmer</p>
    <h1 class="title">
      <span class="title-line title-small line-the">The</span>
      <span class="title-line title-large line-murmurs">Murmurs</span>
      <span class="title-line title-small line-of">of</span>
      <span class="title-line title-largest line-lorient">Lorient</span>
    </h1>
    <p class="publisher">Editions Pluvane</p>
  </main>
</body>
</html>
```